Visitenkarten-Design für architect i.a.
Aufgabenstellung
Logo ( Siehe Anhang)
scrinari
dessignader da construcziun aulta
maturitad professiunla
architect i.a.

```html
<!DOCTYPE html>
<html lang="de">
<head>
<meta charset="utf-8">
<title>Visitenkarte – Torvel Kinst, Architekt i.a.</title>
<link rel="stylesheet" href="https://fonts.googleapis.com/css2?family=Open+Sans:wght@400;600;700&display=swap">
<style>
  :root {
    --page-bg: #ffffff;
    --card-bg: #ffffff;
    --band-light: #8fcdec;
    --band-dark: #4f6774;
    --text-dark: #3c3c3c;
    --text-grey: #5a5a5a;
    --shadow: rgba(0, 0, 0, 0.35);
  }
  * { box-sizing: border-box; margin: 0; padding: 0; }
  html, body {
    width: 1200px; height: 1200px; overflow: hidden;
    background: var(--page-bg);
    font-family: "Open Sans", Arial, sans-serif;
  }
  .sheet { position: relative; width: 1200px; height: 1200px; }
  .card {
    position: absolute; top: 462px;
    width: 420px; height: 276px;
    background: var(--card-bg);
    box-shadow: 10px 12px 12px var(--shadow);
    border: 1px solid #e4e4e4;
    overflow: hidden;
  }
  .card--front { left: 140px; }
  .card--back { left: 630px; }
  .band { position: absolute; top: 45px; height: 18px; }
  .band--light { background: var(--band-light); }
  .band--dark { background: var(--band-dark); }
  .card--front .band--light { left: 0; width: 98px; }
  .card--front .band--dark { left: 213px; width: 207px; }
  .card--back .band--light { left: 0; width: 126px; }
  .card--back .band--dark {
    left: 222px; width: 198px;
    display: flex; align-items: center; gap: 6px; padding-left: 44px;
    color: #ffffff; font-size: 14px; letter-spacing: 0.3px;
  }
  .mark-square {
    position: absolute; top: 22px; width: 60px; height: 60px;
    background: var(--band-light);
  }
  .card--front .mark-square { left: 115px; }
  .card--back .mark-square { left: 133px; }
  .brand-name {
    position: absolute; left: 52px; top: 95px;
    font-size: 40px; font-weight: 600; color: var(--text-grey);
    letter-spacing: -0.5px; line-height: 1;
  }
  .qualifications {
    position: absolute; left: 52px; top: 165px;
    list-style: none; font-size: 15px; line-height: 24px; color: var(--text-dark);
  }
  .address {
    position: absolute; left: 57px; top: 96px;
    font-style: normal; font-size: 15px; line-height: 23px; color: var(--text-dark);
  }
  .email {
    position: absolute; left: 57px; top: 186px;
    font-size: 15px; line-height: 23px; font-weight: 600; color: var(--text-dark);
  }
</style>
</head>
<body>
<main class="sheet">
  <section class="card card--front" aria-label="Vorderseite">
    <div class="band band--light"></div>
    <div class="mark-square"></div>
    <div class="band band--dark"></div>
    <div class="brand-name">kinst architectura</div>
    <ul class="qualifications">
      <li>Designer des Baues aulta</li>
      <li>Maturitad professiunla</li>
      <li>Architekt i.a.</li>
    </ul>
  </section>

  <section class="card card--back" aria-label="Rückseite">
    <div class="band band--light"></div>
    <div class="mark-square"></div>
    <div class="band band--dark">
      <svg class="phone-icon" width="13" height="13" viewBox="0 0 24 24" aria-hidden="true">
        <circle cx="12" cy="12" r="12" fill="#ffffff"/>
        <path d="M8.2 6.5l1.8-.4 1.2 2.9-1.2 1c.6 1.4 1.6 2.5 3 3.1l1-1.2 2.9 1.2-.4 1.8c-.2.6-.8 1-1.4.9-4-.6-7.2-3.8-7.8-7.8-.1-.6.3-1.2.9-1.5z" fill="#4f6774"/>
      </svg>
      <span class="phone">079 555 12 34</span>
    </div>
    <address class="address">
      Torvel Kinst<br>
      Lindenhofweg 17<br>
      6014 Luzern
    </address>
    <div class="email">torvelkinst@alpmail.ch</div>
  </section>
</main>
</body>
</html>
```